50's-style gig poster for a birthday bash

My wife was born in 1957 and is turning 57 next month. I'm throwing a surprise party for her, and thought it would be fun to have a 18x24 poster printed and framed for the event. Attached is a poster from a Rolf Tesker gig in 1957. I'd like something like this, with a tinted B&W head shot of my wife, with similar fonts and background color schemes. The copy will be GRETA at the top (where the name ROLF appears), with 57X57 under it, and the word Celebration where the word Quartet currently appears. The rest of the copy will be provided to you. Thanks for your interest and I look forward to working with you.

```html
<!DOCTYPE html>
<html lang="en">
<head>
<meta charset="utf-8">
<title>GRETA 57X57 Celebration Poster</title>
<link href="https://fonts.googleapis.com/css2?family=Anton&family=Abril+Fatface&family=Fraunces:opsz,wght@144,900&family=Open+Sans:ital,wght@1,700;1,800&display=swap" rel="stylesheet">
<style>
  :root {
    --navy: #1b1862;
    --red: #f0230b;
    --cream: #f8e7c9;
    --white: #ffffff;
    --butter: #f4efa2;
    --backdrop: #e9e9e7;
    --shadow: rgba(0, 0, 0, 0.55);
  }
  * { margin: 0; padding: 0; box-sizing: border-box; }
  html, body {
    width: 1200px;
    height: 1148px;
    overflow: hidden;
    background: var(--backdrop);
  }
  .poster {
    position: absolute;
    left: 200px;
    top: 34px;
    width: 800px;
    height: 1080px;
    background: var(--cream);
    overflow: hidden;
  }
  .stripes {
    position: absolute;
    left: 24px;
    top: 30px;
    width: 752px;
    height: 1016px;
    display: grid;
    grid-template-columns: repeat(5, minmax(0, 1fr));
    column-gap: 6px;
  }
  .stripe--navy { background: var(--navy); }
  .stripe--red { background: var(--red); }

  .letter-row {
    position: absolute;
    left: 24px;
    width: 752px;
    display: grid;
    grid-template-columns: repeat(5, minmax(0, 1fr));
    column-gap: 6px;
    font-family: "Anton", "Impact", sans-serif;
    font-weight: 400;
    color: var(--white);
    text-align: center;
    text-shadow: 6px 6px 6px var(--shadow);
  }
  .letter-row span {
    display: block;
    min-width: 0;
    text-align: center;
  }
  .name-row {
    top: 88px;
    font-size: 176px;
    line-height: 1;
  }
  .age-row {
    top: 240px;
    font-size: 261px;
    line-height: 1;
  }
  .kicker {
    position: absolute;
    left: 50px;
    top: 42px;
    font-family: "Open Sans", Arial, sans-serif;
    font-style: italic;
    font-weight: 800;
    font-size: 22px;
    letter-spacing: 2px;
    color: var(--white);
  }
  .headshot {
    position: absolute;
    left: 84px;
    top: 490px;
    width: 258px;
    height: 310px;
    transform: rotate(-7deg);
    background: linear-gradient(135deg, #1c2030 0%, #5b6478 45%, #c9d0dc 70%, #2a2f3e 100%);
    box-shadow: 6px 8px 10px var(--shadow);
  }
  .event-title {
    position: absolute;
    left: 300px;
    top: 486px;
    font-family: "Fraunces", Georgia, serif;
    font-weight: 900;
    font-size: 56px;
    line-height: 1;
    color: var(--butter);
    transform: rotate(-2deg);
    text-shadow: 4px 4px 5px var(--shadow);
  }
  .featuring {
    position: absolute;
    left: 470px;
    top: 572px;
    font-family: "Open Sans", Arial, sans-serif;
    font-style: italic;
    font-weight: 700;
    font-size: 21px;
    color: var(--white);
  }
  .lineup {
    position: absolute;
    left: 398px;
    top: 600px;
    font-family: "Open Sans", Arial, sans-serif;
    font-weight: 800;
    font-size: 23px;
    line-height: 34px;
    letter-spacing: 0.5px;
    color: var(--white);
    text-shadow: 3px 3px 3px var(--shadow);
  }
  .badge-oval {
    position: absolute;
    left: 440px;
    top: 684px;
    width: 226px;
    height: 148px;
    border-radius: 50%;
    background: var(--cream);
    box-shadow: 5px 6px 8px var(--shadow);
  }
  .support-label {
    position: absolute;
    left: 176px;
    top: 800px;
    font-family: "Open Sans", Arial, sans-serif;
    font-style: italic;
    font-weight: 700;
    font-size: 22px;
    color: var(--white);
  }
  .support-act {
    position: absolute;
    left: 112px;
    top: 818px;
    font-family: "Abril Fatface", "Didot", serif;
    font-size: 80px;
    line-height: 1;
    color: var(--white);
    transform: rotate(-1.5deg);
    text-shadow: 5px 5px 5px var(--shadow);
  }
  .info-panel {
    position: absolute;
    left: 124px;
    top: 912px;
    width: 604px;
    height: 118px;
    background: var(--cream);
    box-shadow: 5px 6px 8px var(--shadow);
  }
</style>
</head>
<body>
  <main class="poster">
    <div class="stripes">
      <div class="stripe stripe--navy"></div>
      <div class="stripe stripe--red"></div>
      <div class="stripe stripe--navy"></div>
      <div class="stripe stripe--red"></div>
      <div class="stripe stripe--navy"></div>
    </div>

    <p class="kicker">THE</p>

    <h1 class="letter-row name-row">
      <span>G</span><span>R</span><span>E</span><span>T</span><span>A</span>
    </h1>

    <p class="letter-row age-row">
      <span>5</span><span>7</span><span>X</span><span>5</span><span>7</span>
    </p>

    <div class="headshot" role="img" aria-label="Tinted black and white head shot of the guest of honour singing"></div>

    <h2 class="event-title">Celebration</h2>

    <p class="featuring">Featuring:</p>
    <p class="lineup">xxxxxxxxxxxxxxxx<br>xxxxxxxxxxxxxxx</p>

    <div class="badge-oval"></div>

    <div class="info-panel"></div>

    <p class="support-label">Also Appearing</p>
    <p class="support-act">Another person</p>
  </main>
</body>
</html>
```